Owner of Clinical Testing Lab/. Pixel Harbor Logo completed. Need Matching business Cards

Im the owner of and need cards for business. Colors fonts and logo already purchased through pixel harbor and have the source files. Like to keep same color format , Include logo one side. My Name Address of Lab. My cell number, Lab telephone number and website address. Want to keep simple.

Target Market(s)

Customers

Industry/Entity Type

HealthCare

Contact Information for Business Card

Dr. Corisande Threlkeld Ph.D. Address: QVT Foundry Campus 4417 Foundry Campus Loop Building 2600 Room 314. Baton Rouge LA 70931. Phone : 555.317.0942

Requirements
Must have
• Logo - Color same

```html
<!DOCTYPE html>
<html lang="en">
<head>
<meta charset="UTF-8">
<title>Norvane Laboratories – Business Card</title>
<link href="https://fonts.googleapis.com/css2?family=Josefin+Sans:wght@400&family=Roboto:wght@400;700&display=swap" rel="stylesheet">
<style>
  :root {
    --backdrop: #d3d6d8;
    --paper: #f1f1ef;
    --navy: #0f3a7c;
    --navy-deep: #0d2f66;
    --teal: #1f9a7a;
    --ink: #3c3f44;
    --white: #f4f5f6;
  }
  * { box-sizing: border-box; margin: 0; padding: 0; }
  html, body {
    width: 1200px; height: 1049px; overflow: hidden;
    background: var(--backdrop);
  }
  .canvas {
    width: 1200px; height: 1049px;
    display: flex; flex-direction: column;
    align-items: center; justify-content: center; gap: 70px;
  }
  .card {
    width: 560px; height: 320px; border-radius: 4px;
    position: relative; overflow: hidden;
    box-shadow: 0 14px 30px rgba(0,0,0,.18);
  }
  .card--front {
    background: var(--paper);
    border-bottom: 4px solid var(--teal);
    display: flex; align-items: center;
    padding: 0 34px 0 38px;
  }
  .card--back {
    background: var(--navy);
    border-bottom: 6px solid var(--teal);
    display: flex; align-items: center; justify-content: center;
  }
  .wordmark {
    display: flex; align-items: center; gap: 12px;
    font-family: "Josefin Sans", sans-serif; font-weight: 400;
    color: var(--navy);
  }
  .wordmark__dot {
    width: 16px; height: 16px; border-radius: 50%;
    background: var(--navy); flex: none;
  }
  .wordmark__name { font-size: 27px; line-height: 1.15; letter-spacing: 1px; }
  .card--back .wordmark { color: var(--white); }
  .card--back .wordmark__dot { background: var(--white); }
  .card--back .wordmark__name { font-size: 40px; }
  .divider {
    width: 2px; height: 200px; background: var(--navy);
    margin: 0 26px; flex: none;
  }
  .contact { font-family: "Roboto", sans-serif; color: var(--ink); }
  .contact__name { font-weight: 700; font-size: 15px; color: var(--navy-deep); }
  .contact__role { font-size: 13px; color: var(--teal); margin-bottom: 12px; }
  .contact__address { font-size: 12px; line-height: 1.45; margin-bottom: 8px; }
  .contact__line {
    display: flex; align-items: center; gap: 7px;
    font-size: 12px; line-height: 1.6;
  }
  .contact__line svg { width: 11px; height: 11px; fill: var(--navy); flex: none; }
</style>
</head>
<body>
<main class="canvas">
  <section class="card card--front">
    <div class="wordmark">
      <span class="wordmark__dot"></span>
      <span class="wordmark__name">Norvane<br>Laboratories</span>
    </div>
    <span class="divider"></span>
    <div class="contact">
      <p class="contact__name">Dr. Corisande Threlkeld Ph.D</p>
      <p class="contact__role">Managing Director</p>
      <p class="contact__address">QVT Foundry Campus 4417<br>Foundry Campus Loop Building 2600<br>Room 314. Baton Rouge LA 70931</p>
      <p class="contact__line">
        <svg viewBox="0 0 12 12"><path d="M1 4c0-2 2-3 5-3s5 1 5 3v1H8V4H4v1H1zM2 6h8l1 5H1z"/></svg>555.317.0942
      </p>
      <p class="contact__line">
        <svg viewBox="0 0 12 12"><path d="M3 0h6v12H3zM4 1.5v8h4v-8z"/></svg>555.482.1163
      </p>
      <p class="contact__line">
        <svg viewBox="0 0 12 12"><path d="M0 2h12v8H0zM1 3l5 4 5-4z"/></svg>corisande@norvane.com
      </p>
      <p class="contact__line">
        <svg viewBox="0 0 12 12"><circle cx="6" cy="6" r="6"/></svg>corisandenorvane.com
      </p>
    </div>
  </section>

  <section class="card card--back">
    <div class="wordmark">
      <span class="wordmark__dot"></span>
      <span class="wordmark__name">Norvane Laboratories</span>
    </div>
  </section>
</main>
</body>
</html>
```